Looking for updated Letterhead and Compliments Slips to go with our new updated logo. This stationary will be used for letters to suppliers and customers so needs to be practical while also quite classic.

We are an engineering company so needs to be clean and precise

Target Market(s)

SME'S and large automotive customers

Industry/Entity Type

Automotive

Font styles to use
Sans Serif

Colors
85acd3
0356a4
0792cd
33a6d7
85abd2
ffffff

Requirements
Must have
• Address details as below
• KT Fabrications Limited
• Marbury Close
• Harlowby
• Westmarsh
• DN47 3XP, UK
• Telephone: +44 (0)1632 960418
• Fax: +44 (0)1632 960735
• Email: sales@ktfabrications.example
• Web: www.ktfabrications.example
Nice to have
• Nice to have some element of being a British Manufacturer

```html
<!DOCTYPE html>
<html lang="en">
<head>
<meta charset="utf-8">
<title>KT Fabrications Limited – Letterhead</title>
<link rel="stylesheet" href="https://fonts.googleapis.com/css2?family=Open+Sans:wght@400;600&display=swap">
<style>
  :root {
    --brand-navy: #0356a4;
    --brand-sky: #85acd3;
    --ink: #231f20;
    --page-edge: #9a9a9a;
    --paper: #ffffff;
  }
  * { margin: 0; padding: 0; box-sizing: border-box; }
  html, body { width: 849px; height: 1200px; overflow: hidden; background: var(--paper); }
  .letterhead {
    position: relative;
    width: 849px;
    height: 1200px;
    border: 1px solid var(--page-edge);
    background: var(--paper);
    font-family: "Open Sans", Arial, sans-serif;
    color: var(--ink);
    overflow: hidden;
  }
  .company-mark {
    position: absolute;
    left: 60px;
    top: 158px;
    display: flex;
    align-items: center;
    gap: 14px;
  }
  .company-mark__dot {
    width: 16px;
    height: 16px;
    border-radius: 50%;
    background: var(--brand-navy);
  }
  .company-mark__name {
    font-size: 24px;
    font-weight: 400;
    letter-spacing: 6.5px;
    line-height: 1;
    color: var(--ink);
    text-transform: uppercase;
    white-space: nowrap;
  }
  .contact-list {
    position: absolute;
    left: 627px;
    top: 130px;
    list-style: none;
    font-size: 12px;
    line-height: 15.2px;
    color: var(--ink);
    white-space: nowrap;
  }
  .contact-list li { display: flex; align-items: center; gap: 5px; }
  .contact-icon { width: 11px; height: 11px; flex: none; }
  .footer-band {
    position: absolute;
    top: 1079px;
    height: 36px;
    background: var(--brand-navy);
  }
  .footer-band--left { left: 0; width: 421px; display: flex; align-items: center; padding-left: 28px; gap: 8px; }
  .footer-band--right { left: 718px; width: 131px; }
  .footer-address {
    font-size: 12.5px;
    color: var(--paper);
    letter-spacing: 0.1px;
    white-space: nowrap;
  }
  .pin-icon { width: 12px; height: 16px; flex: none; }
</style>
</head>
<body>
<main class="letterhead">
  <div class="company-mark">
    <span class="company-mark__dot"></span>
    <span class="company-mark__name">KT Fabrications</span>
  </div>

  <ul class="contact-list">
    <li>
      <svg class="contact-icon" viewBox="0 0 11 11" aria-hidden="true"><rect width="11" height="11" rx="2" fill="#0356a4"/><rect x="3" y="2" width="5" height="7" rx="1" fill="#fff"/></svg>
      <span>+44 (0)1632 960418</span>
    </li>
    <li>
      <svg class="contact-icon" viewBox="0 0 11 11" aria-hidden="true"><rect width="11" height="11" rx="2" fill="#0356a4"/><path d="M2 5h7v4H2z M4 2h3v3H4z" fill="#fff"/></svg>
      <span>+44 (0)1632 960735</span>
    </li>
    <li>
      <svg class="contact-icon" viewBox="0 0 11 11" aria-hidden="true"><rect width="11" height="11" rx="2" fill="#0356a4"/><rect x="2" y="3" width="7" height="5" fill="#fff"/><path d="M2 3l3.5 3L9 3" stroke="#0356a4" fill="none" stroke-width="0.8"/></svg>
      <span>sales@ktfabrications.example</span>
    </li>
    <li>
      <svg class="contact-icon" viewBox="0 0 11 11" aria-hidden="true"><rect width="11" height="11" rx="2" fill="#0356a4"/><circle cx="5.5" cy="5.5" r="3.2" fill="none" stroke="#fff" stroke-width="0.9"/><path d="M2.3 5.5h6.4M5.5 2.3v6.4" stroke="#fff" stroke-width="0.7"/></svg>
      <span>www.ktfabrications.example</span>
    </li>
  </ul>

  <div class="footer-band footer-band--left">
    <svg class="pin-icon" viewBox="0 0 12 16" aria-hidden="true"><path d="M6 0a6 6 0 0 0-6 6c0 4.5 6 10 6 10s6-5.5 6-10a6 6 0 0 0-6-6z" fill="#fff"/><circle cx="6" cy="6" r="2.3" fill="#0356a4"/></svg>
    <span class="footer-address">Marbury Close, Harlowby, Westmarsh, DN47 3XP, UK</span>
  </div>
  <div class="footer-band footer-band--right"></div>
</main>
</body>
</html>
```